Poster Design Project

We are launching a new company Q Vizo, we sell advertising on digital signage and we are launching our company selling ads at our 2 locations, Barlow Heights Sports and Rec Club and the Merrowby Bay Sports and Rec Club. We want to advertise that we have 5 10 and 15 ad slots available and ads start from as little as $27.00 per week. We need to let people know we offer 10% discount to KNBTA members. it needs to have the following contact details to get more information, Marcus 0427359012 and marcus@qvizo.com.au. As a new launch we are offering for the first 10 customers one of 2 discounts, get 4 weeks free all you have to pay is the content creation fee ($99 for 5 second ad) or 4 weeks free and free content creation if you sign up to a 18 week contract.

Update: need the add to start wit something like this but you can be creative:

Need to get you message or brand out, Have you heard of digital sinage?
We have ads avaliable starting from $27 per week at one of our locations.

Or something like that, as i am introducing my company they dont know what i do you untill they read this poster.

Target Market(s)

Targeting small to medium buisness

Industry/Entity Type

Advertising

Requirements
Must have
• Logo

```html
<!DOCTYPE html>
<html lang="en">
<head>
<meta charset="utf-8">
<title>Q Vizo – Digital Signage Poster</title>
<link rel="stylesheet" href="https://fonts.googleapis.com/css2?family=Open+Sans:wght@400;600;700;800&display=swap">
<style>
  :root {
    --page: #ffffff;
    --ink: #111111;
    --white: #ffffff;
    --blue-start: #4dd6ff;
    --blue-end: #0016f2;
    --green-start: #80ff06;
    --green-end: #127c0a;
    --orange-start: #ffb000;
    --orange-end: #ff4400;
    --dark-start: #1e1e1e;
    --dark-end: #000000;
    --rule: #555555;
    --brand-mark: #1e6cf5;
  }
  * { margin: 0; padding: 0; box-sizing: border-box; }
  html, body {
    width: 1200px; height: 1001px; overflow: hidden;
    background: var(--page);
    font-family: "Open Sans", Arial, sans-serif;
  }
  .canvas { position: relative; width: 1200px; height: 1001px; }
  .poster {
    position: absolute; left: 294px; top: 103px; width: 612px; height: 793px;
    background: var(--white);
    box-shadow: 0 0 6px rgba(0,0,0,0.45);
  }
  .brand {
    position: absolute; left: 0; top: 30px; width: 100%; height: 120px;
    display: flex; align-items: center; justify-content: center; gap: 18px;
  }
  .brand-mark { width: 62px; height: 62px; background: var(--brand-mark); }
  .brand-name { font-weight: 800; font-size: 56px; color: var(--ink); letter-spacing: -1px; }

  .band {
    position: absolute; left: 0; width: 100%; height: 109px;
    display: flex; flex-direction: column; justify-content: center; align-items: center;
    color: var(--white); font-size: 35px; line-height: 49px; font-weight: 400;
    text-align: center; letter-spacing: -0.3px;
  }
  .band strong { font-weight: 700; }
  .band-ask { top: 189px; background: linear-gradient(90deg, var(--blue-start), var(--blue-end)); }
  .band-price { top: 314px; background: linear-gradient(90deg, var(--green-start), var(--green-end)); }
  .band-discount { top: 439px; background: linear-gradient(90deg, var(--orange-start), var(--orange-end)); }

  .offer {
    position: absolute; left: 0; top: 595px; width: 100%; height: 198px;
    background: linear-gradient(90deg, var(--dark-start), var(--dark-end));
    color: var(--white);
  }
  .offer-title {
    position: absolute; top: 9px; width: 100%; text-align: center;
    font-size: 21px; font-weight: 600; letter-spacing: -0.2px;
  }
  .offer-terms {
    position: absolute; top: 49px; width: 100%; text-align: center;
    font-size: 12px; line-height: 19px; letter-spacing: -0.3px;
  }
  .offer-terms .or { font-weight: 700; }
  .offer-rule {
    position: absolute; left: 24px; right: 24px; top: 129px;
    height: 1px; background: var(--rule);
  }
  .slots {
    position: absolute; left: 25px; top: 163px; font-size: 14px;
  }
  .slots strong { font-size: 18px; font-weight: 700; }
  .contact {
    position: absolute; right: 24px; top: 134px; text-align: right;
  }
  .contact-phone { font-size: 17px; line-height: 24px; }
  .contact-email { font-size: 20px; line-height: 30px; }
</style>
</head>
<body>
<div class="canvas">
  <main class="poster">
    <header class="brand">
      <span class="brand-mark"></span>
      <span class="brand-name">Q Vizo</span>
    </header>

    <section class="band band-ask">
      <div><strong>ASK US</strong> WHAT <strong>DIGITAL</strong></div>
      <div><strong>SIGNAGE</strong> CAN DO <strong>FOR YOU</strong></div>
    </section>

    <section class="band band-price">
      <div>ADS <strong>START FROM ONLY</strong></div>
      <div><strong>$27.00</strong> per week</div>
    </section>

    <section class="band band-discount">
      <div><strong>10% DISCOUNT</strong></div>
      <div>TO <strong>KNBTA</strong> MEMBERS</div>
    </section>

    <section class="offer">
      <h2 class="offer-title">SPECIAL OFFER FOR THE 10 FIRST NEW CUSTOMERS:</h2>
      <div class="offer-terms">
        <div>GET 4 WEEKS FREE, ONLY PAY FOR THE CONTENT CREATION FEE ($99 FOR 5 SECOND AD)</div>
        <div class="or">OR</div>
        <div>4 WEEKS AND CONTENT CREATION FREE&nbsp; ON 18 WEEKS CONTRACT SIGN UP</div>
      </div>
      <div class="offer-rule"></div>
      <div class="slots">AD SLOTS AVAILABLE : <strong>5,10 ,15</strong></div>
      <div class="contact">
        <div class="contact-phone">Marcus: 0427359012</div>
        <div class="contact-email">marcus@qvizo.com.au</div>
      </div>
    </section>
  </main>
</div>
</body>
</html>
```